VORL Pty Ltd Business Card

Looking for a simple yet eye-catching double-sided business card design using my company logo on one side and contact details on the other.

Target Market(s)

Government

Industry/Entity Type

Communication Systems Engineering

Contact Information for Business Card

VORL Pty Ltd

Requirements
Nice to have
• Would be great to have a QR code so details can be scanned into contacts

```html
<!DOCTYPE html>
<html lang="en">
<head>
<meta charset="utf-8">
<title>VORL Pty Ltd Business Card</title>
<link rel="stylesheet" href="https://fonts.googleapis.com/css2?family=Archivo:wdth,wght@62..125,400..900&family=Arimo:wght@400;700&display=swap">
<style>
  :root {
    --backdrop: #959595;
    --paper: #ffffff;
    --navy: #132a4b;
    --ink: #1b2f52;
    --black: #07090c;
    --band-light: #3d4a68;
    --mark-muted: #9aa0b5;
  }
  * { margin: 0; padding: 0; box-sizing: border-box; }
  html, body { width: 967px; height: 1200px; overflow: hidden; }
  body { background: var(--backdrop); position: relative; font-family: "Arimo", Arial, sans-serif; }

  .card { position: absolute; overflow: hidden; }
  .card--front { left: 117px; top: 154px; width: 738px; height: 426px; background: var(--paper); border: 1px solid var(--navy); border-bottom: none; }
  .card--back { left: 116px; top: 703px; width: 740px; height: 424px; background: var(--navy); }

  .brand { position: absolute; display: flex; align-items: center; gap: 12px; }
  .brand__square { width: 20px; height: 20px; }
  .brand__name { font-family: "Archivo", Arial, sans-serif; font-weight: 800; font-stretch: 125%; font-size: 35px; line-height: 1; letter-spacing: 1px; }

  .card--front .brand { left: 215px; top: 112px; }
  .card--front .brand__square { background: var(--ink); }
  .card--front .brand__name { color: var(--ink); }

  .tagline { position: absolute; left: 116px; top: 184px; font-family: "Archivo", Arial, sans-serif; font-weight: 800; font-stretch: 125%; font-size: 16.5px; letter-spacing: 0.6px; color: var(--ink); white-space: nowrap; }

  .pitch { position: absolute; left: 116px; top: 216px; font-size: 9.6px; line-height: 18.4px; color: var(--ink); letter-spacing: 0.2px; white-space: pre; }
  .pitch p + p { margin-top: 18.4px; }

  .front-bands { position: absolute; left: 0; bottom: 0; width: 738px; height: 48px; }

  .card--back .brand { left: 50%; top: 174px; transform: translateX(-50%); }
  .card--back .brand__square { background: var(--mark-muted); }
  .card--back .brand__name { color: var(--mark-muted); }

  .contact { position: absolute; left: 0; right: 0; top: 251px; text-align: center; color: #ffffff; font-weight: 700; font-size: 9.8px; line-height: 19px; letter-spacing: 0.2px; }

  .back-band { position: absolute; left: 0; top: 374px; width: 100%; height: 17px; background: var(--band-light); }
</style>
</head>
<body>

<section class="card card--front">
  <div class="brand">
    <span class="brand__square"></span>
    <span class="brand__name">VORL</span>
  </div>
  <h1 class="tagline">SYSTEM INTEGRATION SOLUTIONS</h1>
  <div class="pitch">
    <p>let solve your technical issues through
 our knowledge
and experience of systems components
 and engineering.</p>
    <p>At VORL we strive to ensure your missioncritical
teams have teliable assured communications.</p>
  </div>
  <svg class="front-bands" viewBox="0 0 760 50" preserveAspectRatio="none" aria-hidden="true">
    <polygon points="0,0 512,0 498,20 0,20" fill="var(--navy)"/>
    <polygon points="515,0 760,0 760,50 0,50 0,28 497,28" fill="var(--black)"/>
  </svg>
</section>

<section class="card card--back">
  <div class="brand">
    <span class="brand__square"></span>
    <span class="brand__name">VORL</span>
  </div>
  <div class="contact">
    <p>Email: admin@vorl.com.au</p>
    <p>Postal Address: 14- 16 Harlow Lane Kellerton&nbsp; NSW&nbsp; 2150 Australia</p>
  </div>
  <div class="back-band"></div>
</section>

</body>
</html>
```